New Business Card Design Project

I have a logo I would like to use on the business card. I want something that will stand out and that will be remembered.

Target Market(s)

People who collect gems, minerals and crystals.

Contact Information for Business Card

email - mkthestonefalcon@vendrollo.com
phone # 917-406-2581

Font styles to use
Serif
Sans Serif
Decorative

Colors

Designer to choose colors to be used in the design.

Requirements
Must have
• The logo...two to choose from.
Nice to have
• An eye catching and memorable way to draw in people who collect gems minerals and crystals.

```html
<!DOCTYPE html>
<html lang="en">
<head>
<meta charset="utf-8">
<title>The Stone Falcon — Business Card</title>
<link rel="stylesheet" href="https://fonts.googleapis.com/css2?family=Oswald:wght@500;700&display=swap">
<style>
  :root {
    --backdrop: #e6e7eb;
    --royal-blue: #1226a8;
    --deep-blue: #0a1670;
    --ink: #0b0b0d;
    --stone-grey: #d9d9db;
    --paper: #ffffff;
  }
  * { box-sizing: border-box; margin: 0; padding: 0; }
  html, body {
    width: 1200px; height: 863px; overflow: hidden;
    background: var(--backdrop);
    font-family: "Oswald", "Arial Narrow", sans-serif;
  }
  .card-set {
    position: absolute; left: 0; top: 0; width: 1200px; height: 863px;
    display: flex; justify-content: center; align-items: center; gap: 44px;
  }
  .card {
    position: relative; width: 300px; height: 525px; overflow: hidden;
    box-shadow: 0 10px 28px rgba(0,0,0,.22);
  }
  .card-shapes { position: absolute; inset: 0; width: 100%; height: 100%; }
  .wordmark {
    position: absolute; left: 0; right: 0;
    text-align: center; font-weight: 700; font-size: 34px;
    line-height: 1.05; letter-spacing: .5px; text-transform: uppercase;
  }
  .card--front { background: var(--stone-grey); }
  .card--front .wordmark { top: 200px; color: var(--ink); }
  .card--back { background: var(--ink); }
  .card--back .wordmark { top: 150px; color: var(--paper); }
  .name-banner {
    position: absolute; left: 30px; width: 240px; top: 262px; height: 40px;
    background: var(--paper);
    clip-path: polygon(0 0, 100% 0, 94% 100%, 6% 100%);
    display: flex; align-items: center; justify-content: center;
    font-weight: 700; font-size: 21px; color: var(--ink);
    letter-spacing: .5px; text-transform: uppercase;
  }
  .contact-list {
    position: absolute; left: 0; right: 0; top: 330px;
    display: flex; flex-direction: column; align-items: center; gap: 10px;
    color: var(--paper); font-weight: 500;
  }
  .contact-item { display: flex; flex-direction: column; align-items: center; gap: 8px; }
  .contact-icon { width: 26px; height: 26px; }
  .contact-phone { font-size: 19px; letter-spacing: .3px; }
  .contact-email { font-size: 15px; letter-spacing: .2px; }
</style>
</head>
<body>
<main class="card-set">

  <section class="card card--front" aria-label="Card front">
    <svg class="card-shapes" viewBox="0 0 300 525" preserveAspectRatio="none" aria-hidden="true">
      <polygon points="0,0 300,0 300,38 0,78" fill="var(--royal-blue)"/>
      <polygon points="0,400 300,445 300,525 0,525" fill="var(--ink)"/>
    </svg>
    <h1 class="wordmark">The Stone<br>Falcon</h1>
  </section>

  <section class="card card--back" aria-label="Card back">
    <svg class="card-shapes" viewBox="0 0 300 525" preserveAspectRatio="none" aria-hidden="true">
      <polygon points="0,250 300,230 300,525 0,525" fill="var(--royal-blue)"/>
      <polygon points="0,420 300,380 300,525 0,525" fill="var(--deep-blue)" opacity=".45"/>
    </svg>
    <h2 class="wordmark">The Stone<br>Falcon</h2>
    <p class="name-banner">Marcus Kell</p>

    <div class="contact-list">
      <div class="contact-item">
        <svg class="contact-icon" viewBox="0 0 26 26" aria-hidden="true">
          <polygon points="13,1 24,7 24,19 13,25 2,19 2,7" fill="var(--paper)"/>
          <path d="M8 9c0 5 4 9 9 9l1.5-2-2.5-1.5-1.2 1c-1.6-.8-2.8-2-3.6-3.6l1-1.2L10.5 7.5z" fill="var(--royal-blue)"/>
        </svg>
        <span class="contact-phone">917-406-2581</span>
      </div>
      <div class="contact-item">
        <svg class="contact-icon" viewBox="0 0 26 26" aria-hidden="true">
          <polygon points="13,1 24,7 24,19 13,25 2,19 2,7" fill="var(--paper)"/>
          <rect x="7" y="9" width="12" height="8" fill="var(--royal-blue)"/>
          <polyline points="7,9 13,14 19,9" fill="none" stroke="var(--paper)" stroke-width="1.2"/>
        </svg>
        <span class="contact-email">mkthestonefalcon@vendrollo.com</span>
      </div>
    </div>
  </section>

</main>
</body>
</html>
```